Harbourline Refrigeration business card design

We would like a new design for our business card as we have a new logo.
We need generic business card to give our customers with our office details - with the option of making it individualized for each manager

Target Market(s)

Companies and homeowners

Industry/Entity Type

Air Conditioning

Contact Information for Business Card

We are not sure if we want single or double sided it will depend on the design we choose

Colors
33a6d7
0255a3

Requirements
Must have
• Logo
• phone: (08) 8721 5940
• email: harbourserve@tealnet.example
• website: www.harbourlinerefrigeration.example
• AU61420
• BLD472913
Nice to have
• Address - Shed 5/284 Tallis Rd, Carrow Flats SA 5741

```html
<!DOCTYPE html>
<html lang="en">
<head>
<meta charset="utf-8">
<title>Harbourline Refrigeration – Business Card</title>
<link href="https://fonts.googleapis.com/css2?family=Lato:wght@400;700;900&display=swap" rel="stylesheet">
<style>
  :root {
    --backdrop: #646464;
    --navy: #0b3f7e;
    --brand-blue: #0255a3;
    --brand-sky: #33a6d7;
    --ink: #333333;
    --muted: #444444;
    --rule: #d6d6d6;
    --paper: #ffffff;
  }
  * { margin: 0; padding: 0; box-sizing: border-box; }
  html, body { width: 1200px; height: 900px; overflow: hidden; }
  body {
    background: var(--backdrop);
    font-family: "Lato", Arial, sans-serif;
    position: relative;
  }
  .card {
    position: absolute;
    width: 477px;
    height: 293px;
    box-shadow: 2px 3px 4px rgba(0,0,0,0.45);
  }
  .card--front {
    left: 120px; top: 275px;
    background: var(--paper);
    border-radius: 0 46px 0 46px;
  }
  .card--back {
    left: 620px; top: 276px;
    border-radius: 46px 0 46px 0;
    background: radial-gradient(ellipse 62% 72% at 50% 42%, #37a4d8 0%, #1a77bd 45%, #0a4f93 80%, #084888 100%);
  }
  .brand {
    position: absolute;
    display: flex;
    align-items: center;
    gap: 10px;
    font-weight: 900;
    white-space: nowrap;
  }
  .brand__dot { border-radius: 50%; flex: none; }
  .card--front .brand {
    right: 25px; top: 112px;
    color: var(--navy);
    font-size: 25px;
    letter-spacing: -0.3px;
  }
  .card--front .brand__dot { width: 26px; height: 26px; background: var(--brand-sky); }
  .card--back .brand {
    left: 0; right: 0; top: 142px;
    justify-content: center;
    color: var(--paper);
    font-size: 27px;
    letter-spacing: -0.3px;
  }
  .card--back .brand__dot { width: 28px; height: 28px; background: var(--paper); }
  .person { position: absolute; left: 32px; top: 162px; }
  .person__name { font-size: 19px; font-weight: 700; color: var(--navy); line-height: 1.1; }
  .person__role { font-size: 13.5px; color: var(--muted); margin-top: 2px; }
  .person-rule {
    position: absolute; left: 92px; right: 25px; top: 193px;
    height: 1px; background: var(--rule);
  }
  .contacts {
    position: absolute; left: 32px; top: 213px;
    list-style: none; font-size: 14px; color: var(--ink); line-height: 17.5px;
  }
  .contacts li { display: flex; align-items: center; gap: 4px; }
  .contacts svg { width: 11px; height: 11px; fill: var(--navy); flex: none; }
  .address {
    position: absolute; right: 24px; top: 232px;
    text-align: right; font-size: 14px; color: var(--ink); line-height: 18px;
    font-style: normal;
  }
  .licence-rule {
    position: absolute; left: 105px; right: 105px; top: 231px;
    height: 1px; background: rgba(255,255,255,0.3);
  }
  .licences {
    position: absolute; left: 0; right: 0; top: 246px;
    text-align: center; color: var(--paper); font-size: 13px;
  }
  .licences__sep { margin: 0 16px; }
</style>
</head>
<body>
  <section class="card card--front" aria-label="Business card front">
    <div class="brand"><span class="brand__dot"></span>Harbourline Refrigeration</div>
    <div class="person">
      <p class="person__name">Dara Whitlow</p>
      <p class="person__role">Manager</p>
    </div>
    <div class="person-rule"></div>
    <ul class="contacts">
      <li><svg viewBox="0 0 12 12" aria-hidden="true"><path d="M1 4c0-2 2-3 5-3s5 1 5 3v1H8.5V3.8h-5V5H1zM2.5 6l1.5-1.5h4L9.5 6v4h-7z"/></svg>(08) 8721 5940</li>
      <li><svg viewBox="0 0 12 12" aria-hidden="true"><path d="M1 2.5h10v7H1zM1.6 3.2 6 6.6l4.4-3.4"/><path d="M1.6 3.2 6 6.6l4.4-3.4" stroke="#fff" stroke-width="1" fill="none"/></svg>harbourserve@tealnet.example</li>
      <li><svg viewBox="0 0 12 12" aria-hidden="true"><circle cx="6" cy="6" r="5"/><path d="M3 4.5c1 0 1.5.8 1.3 1.8.8.4 1 1.3.8 2.2M7 2c0 1 .8 1.4 1.8 1.3" stroke="#fff" stroke-width="1" fill="none"/></svg>www.harbourlinerefrigeration.example</li>
    </ul>
    <address class="address">Shed 5/284 Tallis Rd<br>Carrow Flats SA 5741</address>
  </section>

  <section class="card card--back" aria-label="Business card back">
    <div class="brand"><span class="brand__dot"></span>Harbourline Refrigeration</div>
    <div class="licence-rule"></div>
    <p class="licences">AU61420<span class="licences__sep">|</span>BLD472913</p>
  </section>
</body>
</html>
```